Personal Trainer Business Card

I need a business card using a logo I already have.
The logo is in uploaded files.
Card is to give to prospective clients that interested in health and beauty or already exercise. Would like logo on front or other abstract images and details on back.
Like modern design that also unique and eye catching rather than just generic fitness gym/fitness theme.

Target Market(s)

Main clients are trendy women aged 25-60.

Industry/Entity Type

Fitness

Contact Information for Business Card

Email: marc@marcbrevittfitness.com

web: www.marcbrevittfitness.com

mobile: 0432 759208

facebook: www.facebook.com/marcbrevittfitness

Location is: Sunshine Coast

Font styles to use
Sans Serif

Colors
000000
1b1b1b
333333

Requirements
Must have
• Logo on front
• black background of sorts on front (fine if mixed with dark grey or abstract)
• White background on back.
Nice to have
• I would like the front side with the logo appearing on it with black background. Fine with alternative ideas and layout.
• Would like the front to be modern, professional and cool/interesting.
• Fine with abstract or modern design.
• Reverse of the card some white background with details on it
• (I like simple fonts).
• CAn use same font colour as in logo in places or what whatever
Should not have
• Avoiding use of cheap pics such as weights

```html
<!DOCTYPE html>
<html lang="en">
<head>
<meta charset="utf-8">
<title>Marc Brevitt Fitness – Business Cards</title>
<link rel="stylesheet" href="https://fonts.googleapis.com/css2?family=Open+Sans:wght@400&display=swap">
<style>
  :root {
    --page-bg: #e9e6e1;
    --card-front: #1b1b1b;
    --card-back: #ffffff;
    --card-shadow: rgba(0, 0, 0, 0.28);
    --gold: #c8a35a;
    --ink: #333333;
  }
  * { margin: 0; padding: 0; box-sizing: border-box; }
  html, body {
    width: 1200px;
    height: 900px;
    overflow: hidden;
    background: var(--page-bg);
    font-family: "Open Sans", Arial, sans-serif;
  }
  .canvas {
    position: relative;
    width: 1200px;
    height: 900px;
  }
  .card {
    position: absolute;
    width: 540px;
    height: 330px;
    border-radius: 3px;
    box-shadow: 0 10px 28px var(--card-shadow);
    display: flex;
    flex-direction: column;
    align-items: center;
  }
  .card--front { left: 70px; top: 90px; background: var(--card-front); }
  .card--back { left: 590px; top: 480px; background: var(--card-back); }

  .brand {
    display: flex;
    align-items: center;
    gap: 12px;
    margin-top: 104px;
    color: var(--gold);
    font-size: 32px;
    font-weight: 400;
    line-height: 1;
    white-space: nowrap;
  }
  .brand__mark {
    width: 22px;
    height: 22px;
    background: var(--gold);
  }

  .social {
    margin-top: 58px;
    display: flex;
    flex-direction: column;
    align-items: center;
    gap: 8px;
    color: var(--gold);
    font-size: 15px;
  }
  .social__marker {
    width: 12px;
    height: 12px;
    background: var(--gold);
    border-radius: 2px;
  }

  .contact {
    margin-top: 52px;
    display: flex;
    flex-direction: column;
    align-items: center;
    color: var(--ink);
    font-size: 15px;
    line-height: 1.35;
  }
  .contact__icons {
    display: flex;
    gap: 6px;
    margin-bottom: 6px;
  }
  .contact__icons svg { width: 14px; height: 14px; fill: var(--ink); }
</style>
</head>
<body>
<main class="canvas">

  <section class="card card--front">
    <div class="brand">
      <span class="brand__mark"></span>
      <span class="brand__name">Marc Brevitt Fitness</span>
    </div>
    <div class="social">
      <span class="social__marker"></span>
      <span class="social__handle">marcbrevittfitness</span>
    </div>
  </section>

  <section class="card card--back">
    <div class="brand">
      <span class="brand__mark"></span>
      <span class="brand__name">Marc Brevitt Fitness</span>
    </div>
    <div class="contact">
      <div class="contact__icons">
        <svg viewBox="0 0 14 14" aria-label="Phone"><path d="M1 4c0-1.5 2.5-2.5 6-2.5s6 1 6 2.5v1.2h-3V4H4v1.2H1zM3.5 6.5h7L12 12H2z"/></svg>
        <svg viewBox="0 0 14 14" aria-label="Email"><path d="M1 3h12v8H1zM2 4l5 3.8L12 4z" fill-rule="evenodd"/></svg>
        <svg viewBox="0 0 14 14" aria-label="Website"><circle cx="7" cy="7" r="6"/></svg>
      </div>
      <span class="contact__phone">0432 759208</span>
      <span class="contact__email">marc@marcbrevittfitness.com</span>
      <span class="contact__web">www.marcbrevittfitness.com</span>
    </div>
  </section>

</main>
</body>
</html>
```